Film Poster Design For Japanese Film Poster #2

The title of this colour film is KAZE YAMA TSUKI HOSHI春 夏 秋 冬Translated this is literallySpring Summer Fall Winter ... however the English title is FOUR SEASONSWe attached a series of screen shots from the film and also the computer generated Kanji characters. We will be updating the brief with the Japanese title characters which currently being hand painted.We require the post in two formats. One being the traditional poster format and the other being in a wide screen ration of 1000px by 465px. Same design.This is a drama, feature length film comprising of four separate stories. The is mixture of Japanese and English dialogue. We are looking at 2 possible designs. You can choose to submit either.1: A with lots of white space ... focussing on smaller images at the Japanese text. I have uploaded a sample poster as a very rough indication. "Stories nobody ever wrote down about the quiet ones" / "Odile Bettina Rue Ingrid" - Lots of white space.Ideally we would have liked to have had the image of the young girl in the kimono pulling on the bell rope clear cut and used on white as a single main image. However, we are not sure that the clarity or resolution of the original image is sufficient. 2: One with lots of images as you can see with the two "Bridge Of Dust" Sample posters.Obviously we are not looking for a copy of either poster, but these posters are a guide to the two looks we are after.Thanks. Kaede
Hello all,Apologies for the delay. We have had to work through some naming issues.The film's English title has had to be renamed to THE LANTERNS. Please do not used TEN LANTERNS in any designed moving forward.Thanks Kaede Added Sunday, May 25, 2014

```html
<!DOCTYPE html>
<html lang="en">
<head>
<meta charset="utf-8">
<title>KAZE YAMA TSUKI HOSHI — THE LANTERNS</title>
<link rel="stylesheet" href="https://fonts.googleapis.com/css2?family=Noto+Sans+JP:wght@700&family=Oswald:wght@500;600&display=swap">
<style>
  :root {
    --bg-top: #8a8a8a;
    --bg-mid: #c6c6c6;
    --bg-bottom: #f0f0f0;
    --ink: #161616;
    --tone-pink: #e48cc0;
    --tone-rose: #b64f8c;
    --tone-violet: #7a3a86;
    --tone-plum: #4a1e4e;
    --tone-night: #150c18;
    --tone-blue: #6a5fa8;
  }
  * { margin: 0; padding: 0; box-sizing: border-box; }
  html, body { width: 802px; height: 1200px; overflow: hidden; }
  body { font-family: "Oswald", sans-serif; color: var(--ink); }

  .poster {
    position: relative;
    width: 802px;
    height: 1200px;
    background: linear-gradient(180deg, var(--bg-top) 0%, var(--bg-mid) 48%, var(--bg-bottom) 100%);
    overflow: hidden;
  }

  .title-glyph {
    position: absolute;
    top: 150px;
    left: 0;
    width: 802px;
    text-align: center;
    font-family: "Noto Sans JP", sans-serif;
    font-weight: 700;
    font-size: 610px;
    line-height: 1;
    background:
      radial-gradient(ellipse 180px 120px at 30% 18%, var(--tone-pink) 0%, transparent 70%),
      radial-gradient(ellipse 150px 110px at 72% 26%, var(--tone-pink) 0%, transparent 70%),
      radial-gradient(ellipse 220px 90px at 55% 45%, var(--tone-rose) 0%, transparent 75%),
      radial-gradient(ellipse 160px 140px at 22% 55%, var(--tone-violet) 0%, transparent 70%),
      radial-gradient(ellipse 120px 60px at 62% 68%, var(--tone-blue) 0%, transparent 75%),
      radial-gradient(ellipse 260px 100px at 50% 88%, var(--tone-night) 0%, transparent 80%),
      linear-gradient(180deg, var(--tone-rose) 0%, var(--tone-violet) 40%, var(--tone-plum) 70%, var(--tone-night) 100%);
    -webkit-background-clip: text;
    background-clip: text;
    color: transparent;
  }

  .title-romaji {
    position: absolute;
    top: 842px;
    left: 0;
    width: 802px;
    text-align: center;
    font-weight: 600;
    font-size: 50px;
    letter-spacing: 3px;
    line-height: 1;
  }

  .title-english {
    position: absolute;
    top: 912px;
    left: 0;
    width: 802px;
    text-align: center;
    font-weight: 500;
    font-size: 18px;
    letter-spacing: 6px;
    line-height: 1;
  }

  .credits {
    position: absolute;
    top: 1082px;
    left: 0;
    width: 802px;
    text-align: center;
  }
  .credits__roles {
    font-weight: 500;
    font-size: 24px;
    letter-spacing: 2px;
    line-height: 1;
  }
  .credits__block {
    width: 470px;
    margin: 10px auto 0;
    font-weight: 500;
    font-size: 9.5px;
    line-height: 1.4;
    letter-spacing: 0.6px;
    text-transform: uppercase;
  }
</style>
</head>
<body>
  <main class="poster">
    <div class="title-glyph" role="img" aria-label="Kanji 星 filled with a blurred violet and pink film still">星</div>
    <h1 class="title-romaji">KAZE YAMA TSUKI HOSHI</h1>
    <p class="title-english">THE LANTERNS</p>
    <section class="credits">
      <p class="credits__roles">REALISATOR - PRODUCER - EXECUTIVE PROD</p>
      <p class="credits__block">Written and directed by Kaede. Produced with the support of a small film fund. Camera, sound and editing by the house crew. Music performed by a quartet from the hills. Costumes by local makers. A feature in four parts about wind, mountains, the moon and the stars, told quietly.</p>
    </section>
  </main>
</body>
</html>
```